LoomTrellis business card & letterhead
LoomTrellis letterhead and envelopes
I want to thank everyone for your great artwork. I really appreciate all of the inputs. Thank you again.
Pls check private message
Thanks
Paloma pixel
Nice drafts. Thank you all. Keep them coming. Please do not place a bar in the middle of the card.
Again: the title after the name is Ed.S.
So: Howard Winslow Ed.S.
I like the swirl (cycle) better than the straight lines.
Just keep it to single sided please.
Ok, I forgot to put my degree on the guide. It should be: Howard Winslow Ed.S.

```html
<!DOCTYPE html>
<html lang="en">
<head>
<meta charset="utf-8">
<title>LoomTrellis Stationery</title>
<link rel="stylesheet" href="https://fonts.googleapis.com/css2?family=Roboto:wght@400;700&display=swap">
<style>
  :root {
    --stage: #ebe8e1;
    --paper: #ffffff;
    --ink: #111111;
    --ink-soft: #555555;
    --blue: #2f5f9c;
    --blue-light: #4d7fc0;
    --card-text: #d8d8d8;
    --mark: #d9a23a;
    --faint: rgba(120, 160, 90, 0.12);
  }
  * { margin: 0; padding: 0; box-sizing: border-box; }
  html, body { width: 1200px; height: 995px; overflow: hidden; }
  body {
    background: var(--stage);
    font-family: "Roboto", Arial, sans-serif;
    position: relative;
  }
  .piece { position: absolute; box-shadow: 0 4px 14px rgba(0,0,0,0.18); }
  .brand {
    display: flex; align-items: center; gap: 7px;
    font-weight: 700; color: var(--ink); white-space: nowrap;
  }
  .brand-dot { border-radius: 50%; background: var(--mark); flex: none; }
  .faint-ring {
    position: absolute; border-radius: 50%;
    border: 18px solid var(--faint);
  }
  .waves { position: absolute; left: 0; bottom: 0; width: 100%; display: block; }

  /* Envelope */
  .envelope { left: 83px; top: 245px; width: 502px; height: 325px; box-shadow: none; }
  .envelope-flap { position: absolute; left: 0; top: 0; width: 502px; height: 62px; }
  .envelope-body {
    position: absolute; left: 0; top: 60px; width: 502px; height: 265px;
    background: var(--paper); overflow: hidden; box-shadow: 0 4px 14px rgba(0,0,0,0.18);
  }
  .envelope .brand { position: absolute; left: 40px; top: 28px; font-size: 15px; }
  .envelope .brand-dot { width: 14px; height: 14px; }
  .flap-brand {
    position: absolute; left: 250px; top: 20px; transform: rotate(180deg);
    font-size: 11px; color: var(--paper);
  }
  .flap-brand .brand-dot { width: 9px; height: 9px; }
  .return-address {
    position: absolute; left: 40px; top: 66px;
    font-size: 8px; line-height: 12px; color: var(--ink-soft); font-style: normal;
  }
  .envelope .faint-ring { left: 180px; top: 40px; width: 130px; height: 130px; }

  /* Letterhead */
  .letterhead { left: 515px; top: 139px; width: 375px; height: 631px; background: var(--paper); overflow: hidden; }
  .letterhead .brand { position: absolute; left: 28px; top: 44px; font-size: 20px; }
  .letterhead .brand-dot { width: 20px; height: 20px; }
  .letterhead-phone { position: absolute; right: 22px; top: 52px; font-size: 9px; color: var(--ink); }
  .letterhead .faint-ring { left: 100px; top: 230px; width: 190px; height: 190px; border-width: 26px; }
  .letterhead-footer-line {
    position: absolute; left: 16px; top: 556px; font-size: 7.5px; color: var(--ink);
    transform: rotate(-7deg); transform-origin: left center; white-space: nowrap;
  }

  /* Business card */
  .business-card { left: 806px; top: 286px; width: 307px; height: 173px; background: var(--ink); overflow: hidden; }
  .business-card .brand { position: absolute; left: 18px; top: 16px; font-size: 11px; color: var(--paper); }
  .business-card .brand-dot { width: 10px; height: 10px; }
  .business-card .faint-ring { left: 95px; top: 18px; width: 80px; height: 80px; border-width: 10px; border-color: rgba(200,200,120,0.12); }
  .card-contact {
    position: absolute; left: 18px; top: 44px;
    font-size: 6.5px; line-height: 10px; color: var(--card-text); font-style: normal;
  }
  .card-person { position: absolute; left: 170px; top: 62px; color: var(--paper); }
  .card-name { font-size: 9px; font-weight: 700; letter-spacing: 0.5px; }
  .card-title { font-size: 8px; color: var(--card-text); margin-top: 4px; }
</style>
</head>
<body>

<section class="piece envelope" aria-label="Envelope">
  <svg class="envelope-flap" viewBox="0 0 502 62" preserveAspectRatio="none">
    <path d="M0 62 L120 4 Q130 0 145 0 L360 0 Q375 0 385 4 L502 62 Z" fill="#111"/>
  </svg>
  <div class="brand flap-brand"><span class="brand-dot"></span>LoomTrellis</div>
  <div class="envelope-body">
    <div class="faint-ring"></div>
    <div class="brand"><span class="brand-dot"></span>LoomTrellis</div>
    <address class="return-address">
      Address:<br>
      4471 Orchard Ridge Rd.<br>
      Brookvale, TN 38573<br>
      Phone: 901-555-0172<br>
      hwinslow738@loomtrellis.com<br>
      www.loomtrellis.com
    </address>
    <svg class="waves" viewBox="0 0 502 90" preserveAspectRatio="none" height="90">
      <path d="M0 40 Q200 10 502 30 L502 90 L0 90 Z" fill="var(--blue)"/>
      <path d="M0 55 Q220 22 502 44 L502 90 L0 90 Z" fill="#111"/>
      <path d="M0 48 Q210 16 502 36" stroke="var(--blue-light)" stroke-width="3" fill="none"/>
    </svg>
  </div>
</section>

<section class="piece letterhead" aria-label="Letterhead">
  <div class="faint-ring"></div>
  <div class="brand"><span class="brand-dot"></span>LoomTrellis</div>
  <p class="letterhead-phone">Phone: 901-555-0172</p>
  <p class="letterhead-footer-line">Address: 4471 Orchard Ridge Rd. Brookvale, TN 38573 &nbsp;E-mail: hwinslow738@loomtrellis.com</p>
  <svg class="waves" viewBox="0 0 375 90" preserveAspectRatio="none" height="90">
    <path d="M0 45 Q180 40 375 8 L375 90 L0 90 Z" fill="var(--blue)"/>
    <path d="M0 58 Q190 52 375 22 L375 90 L0 90 Z" fill="#111"/>
    <path d="M0 52 Q185 46 375 15" stroke="var(--blue-light)" stroke-width="3" fill="none"/>
  </svg>
</section>

<section class="piece business-card" aria-label="Business card">
  <div class="faint-ring"></div>
  <div class="brand"><span class="brand-dot"></span>LoomTrellis</div>
  <address class="card-contact">
    4471 Orchard Ridge Rd.<br>
    Brookvale, TN 38573<br>
    Phone: 901-555-0172<br>
    hwinslow738@loomtrellis.com<br>
    www.loomtrellis.com
  </address>
  <div class="card-person">
    <p class="card-name">HOWARD WINSLOW Ed.S.</p>
    <p class="card-title">Educational Consultant</p>
  </div>
  <svg class="waves" viewBox="0 0 307 50" preserveAspectRatio="none" height="50">
    <path d="M0 30 Q150 0 307 18 L307 50 L0 50 Z" fill="var(--blue)"/>
    <path d="M0 40 Q160 12 307 30 L307 50 L0 50 Z" fill="#0a0a0a"/>
  </svg>
</section>

</body>
</html>
```